Update Existing Homepage

Here’s the scoop… we want to update our homepage here with a more modern look: wws.Pagelore-Hub.com

I am NOT looking for a brand new design; as our site has many pages, and section. Instead I want a new more modern design based on the existing design (if that make sense)

Whatever new design…must match the rest of the site
I want the current header (menu and up) as well as the current footer to stay the same; it’s everything in between that has to change.

What I’m really looking for is:

- Better use of space
- Better emphasis on key components
- Addition of a new section (more about that below)
- More modern feel

By modern I mean the icons we use are getting a bit cheesy, the straight layout is also dated, etc

Here are the elements that I need to have on the page in ORDER OF IMPORTANCE:

1) ADVERTISING SPACE: while I don’t want huge flashing ads front and center, this being an information site, ads are our #1 source of revenue and as such are important. I would like to see several add slots of various sizes (standard sizes) throughout the page in eye catching spots (not hidden in the bottom right corner)

2) ARTICLES: articles are our main draw. If you look at the current design you will see there is a lead article at the top left of the page and then a series of other articles down the middle

3) NEWSLETTER SUBSCRIPTION BOX: need to have a section that is highly visible for people to subscribe to our newsletter (doesn’t have to be as big as the existing one)

4) BLOG POSTS (‘the experts say’ section): besides articles we also have blog posts. However I’m thinking we could combine the articles and the blog posts into 1 section titled “news” or something to save space. And the blog posts could just have an identifier at the beginning of the title such as “Blog: post title”

5) VIDEOS: don’t need to show a ton of vids, but would like room for 1 main video and a few suggestions of others.

What I have seen a bunch of new websites use is a type rotating ‘newsboard’, like the one on the quorvex homepage for example. Perhaps using an idea like that could be cool. You could feature 1 article, 1 blog post, 1 video, or something in it and have it rotate.

6) RESOURCES: This is something that is not ‘really’ currently on the homepage. By that I mean there is a “webmaster resources” section + a “webmaster tools” section but these are dated. Dated because we recently added a new directory to the site: http://resources.pagelore-hub.com/ - so what I would like to do now is combine those 2 section; 1) invite people to check out the directory + submit there and 2) list a few of the newer entries (ie. new entries automatically get posted on the section of our homepage

7) FORUM DISCUSSIONS: if you look at the “Industry Discussions and Help” section, those are the latest discussions from our forums http://forums.pagelore-hub.com/

That is it…good luck,

Tev

Target Market(s)

web professionals

Industry/Entity Type

Industry

Requirements
Must have
• see description
Nice to have
• see description
Should not have
• see description

```html
<!DOCTYPE html>
<html lang="en">
<head>
<meta charset="utf-8">
<title>Pagelore-Hub — Helping You Succeed Online</title>
<link rel="stylesheet" href="https://fonts.googleapis.com/css2?family=Arimo:wght@400;700&display=swap">
<style>
:root{
  --lime:#c8dc2a;
  --lime-light:#e2ee7a;
  --lime-dark:#9fb314;
  --olive-text:#8a9a12;
  --blue:#1a6fc0;
  --blue-tab:#2a8ae0;
  --link:#1d5fa8;
  --text:#333;
  --line:#ddd;
  --panel:#e8e8e8;
  --ad-text:#a9a9a9;
}
*{box-sizing:border-box;margin:0;padding:0}
html,body{width:686px;height:1200px;overflow:hidden;background:#fff}
body{position:relative;font-family:"Arimo",Arial,sans-serif;color:var(--text);font-size:8px}
.abs{position:absolute}
a{color:var(--link);text-decoration:none}

/* header */
.header{left:38px;top:10px;width:608px;height:65px;border:1px solid #eee;border-bottom:0;background:linear-gradient(#fff,#f7f7f7)}
.brand{left:93px;top:38px;font-size:17px;font-weight:700;color:#444;display:flex;align-items:center;gap:6px}
.brand-dot{width:12px;height:12px;border-radius:50%;background:var(--lime)}
.tagline{left:93px;top:58px;font-size:10px;color:#888;letter-spacing:.5px}
.search{left:371px;top:19px;width:262px;height:24px;background:#e4e4e4;border-radius:3px}
.search-input{left:400px;top:25px;width:150px;height:12px;background:#fff;border:1px solid #ccc}
.search-btn{left:577px;top:20px;width:56px;height:22px;background:var(--lime);border:1px solid var(--lime-dark);font-size:7px;color:#333;text-align:center;line-height:20px}
.lang{left:594px;top:57px;font-size:9px;color:#555;display:flex;gap:4px;align-items:center}
.lang i{width:8px;height:8px;border-radius:50%;background:var(--blue);display:inline-block}

/* nav */
.nav{left:0;top:75px;width:686px;height:27px;background:linear-gradient(#fff,#ececec);border-top:1px solid #ddd;border-bottom:1px solid #ccc}
.nav ul{position:absolute;left:43px;top:0;display:flex;list-style:none;height:26px}
.nav li{font-size:8px;font-weight:700;color:#222;line-height:26px;text-align:center;border-right:1px solid #ccc}
.nav li.active{background:var(--lime)}
.nav-band{left:43px;top:102px;width:601px;height:18px;background:linear-gradient(var(--lime-light),var(--lime))}

/* feature */
.feature{left:43px;top:135px;width:393px;height:175px;border:1px solid var(--line)}
.ftab{position:absolute;left:0;width:101px;height:58px;color:#fff;font-size:12px;display:flex;align-items:center;gap:8px;padding-left:10px}
.ftab svg{flex:none}
.ftab.articles{top:0;background:linear-gradient(#4aa4ee,var(--blue-tab))}
.ftab.videos{top:58px;background:linear-gradient(#9a9a9a,#777)}
.ftab.blog{top:116px;height:58px;background:linear-gradient(#a5a5a5,#868686);line-height:14px}
.f-body{left:112px;top:9px;width:270px}
.kicker{font-size:7px;color:var(--olive-text);text-transform:uppercase}
.f-title{font-size:11.5px;color:var(--olive-text);margin-top:6px;line-height:14px}
.f-meta{font-size:7px;font-weight:700;color:#888;margin-top:12px;line-height:11px}
.f-text{font-size:7.4px;color:#555;margin-top:12px;line-height:11.5px}
.more{font-size:7px;font-weight:700;color:var(--link)}
.more::before{content:"➜ ";}

/* news */
.bar{height:31px;background:linear-gradient(var(--lime-light),var(--lime));border:1px solid #d4e07a;font-size:12px;color:#333;padding-left:44px;line-height:30px}
.news-bar{left:43px;top:325px;width:393px}
.social{position:absolute;top:7px;width:16px;height:16px;border-radius:2px}
.tabs{left:45px;top:369px;display:flex;gap:2px}
.tabs span{font-size:7.5px;color:#555;background:#e6e6e6;border:1px solid #ccc;padding:3px 3px;text-transform:uppercase}
.tabs span.on{background:#fff}
.tabs-line{left:43px;top:385px;width:393px;border-top:1px solid #ccc}
.news-item{left:43px;width:393px;border-bottom:1px solid var(--line)}
.avatar{position:absolute;left:2px;width:24px;height:24px;border-radius:50%;background:radial-gradient(#e9b48c,#b06a3c)}
.doc{position:absolute;left:3px;width:20px;height:22px;background:#f2f2f2;border:1px solid #aaa;border-radius:2px}
.news-item .kicker{position:absolute;left:34px}
.news-item .title{position:absolute;left:32px;font-size:11px;color:var(--link);line-height:15px;width:350px}
.more-box{left:43px;top:587px;width:393px;height:65px;background:var(--panel);padding:9px 8px}
.more-box h4{font-size:8px;color:#333;margin-bottom:6px}
.more-box li{list-style:none;font-size:6.5px;font-weight:700;color:var(--link);line-height:11px}
.more-box li::before{content:"➜ ";}

/* ads */
.ad{border:1px solid #e4e4e4;background:#fff}
.ad small{position:absolute;left:8px;top:3px;font-size:6px;color:#999}
.ad-fill{position:absolute;background:linear-gradient(#e6e6e6,#d9d9d9);color:var(--ad-text);font-size:14px;line-height:16px;padding:5px 6px}
.text-ads{left:448px;top:322px;width:172px;height:150px}
.text-ad{margin-bottom:10px}
.text-ad b{font-size:8px;color:var(--link);text-decoration:underline}
.text-ad p{font-size:8.4px;color:#222;line-height:10px}
.text-ad em{font-style:normal;font-size:5.5px;color:var(--link)}
.pager{left:448px;top:469px;display:flex;gap:2px}
.pager i{width:8px;height:8px;border:1px solid #aaa;display:block;background:#fff}

/* newsletter */
.nl-bar{left:448px;top:487px;width:196px;padding-left:6px}
.nl-intro{left:448px;top:526px;width:196px;font-size:7.2px;color:#555;line-height:11px}
.field label{display:block;font-size:8px;font-weight:700;color:#333}
.field i{display:block;margin-top:4px;width:196px;height:15px;border:1px solid #ccc;background:linear-gradient(#f0f0f0,#fff)}
.privacy{left:448px;top:673px;width:196px;font-size:7.2px;color:#666;line-height:11px}
.subscribe{left:462px;top:701px;width:166px;height:21px;background:linear-gradient(var(--lime-light),var(--lime));border:1px solid var(--lime-dark);border-radius:3px;text-align:center;font-size:10px;line-height:19px;color:#333}

/* resources / forums */
.res-bar{left:43px;top:732px;width:189px;padding-left:8px}
.forum-bar{left:245px;top:732px;width:191px;padding-left:8px}
.sub-h{font-size:8px;font-weight:700;color:#222}
.res-text{left:43px;top:790px;width:192px;font-size:7.3px;color:#777;line-height:11px}
.tile{top:842px;width:90px;height:76px;border-radius:4px;background:linear-gradient(#aaa,#888);color:#eee;font-size:9px;font-weight:700;text-align:center;line-height:12px;padding-top:40px;border:1px solid #777}
.latest-h{left:43px;top:928px;width:189px;height:28px;background:linear-gradient(#fff,#eaeaea);font-size:12px;color:#444;padding:7px 5px;border-bottom:1px solid #ccc}
.res-list{left:43px;top:960px}
.res-list li{list-style:none;font-size:11px;color:var(--link);line-height:20px;display:flex;align-items:center;gap:6px}
.gear{width:13px;height:13px;border-radius:50%;border:3px dotted #aaa}
.forum-list{left:245px;top:792px;width:172px}
.forum-list li{list-style:none;font-size:11px;color:var(--link);line-height:12px;display:flex;gap:7px;margin-bottom:8px}
.bubble{flex:none;width:15px;height:12px;margin-top:1px}
.rule{border-top:1px solid var(--line)}

/* footer */
.footer{left:0;top:1128px;width:686px;height:72px;background:linear-gradient(#e6e6e6,#fff 40%);border-top:1px solid #ddd}
.foot-links{left:0;top:1155px;width:686px;text-align:center;font-size:8px;color:#444}
.copyright{left:0;top:1180px;width:686px;text-align:center;font-size:8px;color:#444}
</style>
</head>
<body>

<header>
  <div class="abs header"></div>
  <div class="abs brand">Pagelore Hub <span class="brand-dot"></span></div>
  <div class="abs tagline">Helping You Succeed Online</div>
  <div class="abs search"></div>
  <div class="abs search-input"></div>
  <div class="abs search-btn">Quick Search</div>
  <div class="abs lang"><i></i>English</div>
</header>

<nav class="abs nav">
  <ul>
    <li class="active" style="width:53px">Home</li>
    <li style="width:58px">Forums</li>
    <li style="width:57px">Videos</li>
    <li style="width:58px">Articles</li>
    <li style="width:77px">Publications</li>
    <li style="width:68px">SEO Blog</li>
    <li style="width:89px">Marketing Blog</li>
    <li style="width:71px">Resources</li>
    <li style="width:70px;border-right:0">Advertise</li>
  </ul>
</nav>
<div class="abs nav-band"></div>

<!-- newsboard -->
<section class="abs feature">
  <div class="ftab articles"><svg width="18" height="20"><rect x="1" y="1" width="15" height="18" rx="2" fill="#fff" stroke="#c68a2e"/><path d="M4 6h9M4 10h9M4 14h6" stroke="#999"/></svg>Articles</div>
  <div class="ftab videos"><svg width="18" height="16"><rect x="1" y="3" width="16" height="12" fill="#222"/><path d="M1 3l4-3h12l-4 3z" fill="#555"/></svg>Videos</div>
  <div class="ftab blog"><svg width="18" height="20"><rect x="1" y="1" width="15" height="18" fill="#f2f2f2" stroke="#bbb"/><path d="M4 6h9M4 10h9M4 14h9" stroke="#ccc"/></svg>Blog<br>posts</div>
  <div class="abs f-body">
    <div class="kicker">Articles</div>
    <div class="f-title">5 Reasons to Build Multiple Niche Websites and Leverage Them</div>
    <div class="f-meta">Published on May 14, 2010<br>by Dana Elworth</div>
    <div class="f-text">Multiple niche websites are a great way to cover all aspects of a business and expand your market reach. Having multiple websites which cover a lot of ground for one business is the latest trend in the field of search engine optimization.</div>
  </div>
  <a class="abs more" style="left:112px;top:155px">Read more</a>
  <a class="abs more" style="left:318px;top:155px">See all articles</a>
</section>

<!-- news -->
<section>
  <div class="abs bar news-bar">News
    <svg class="abs" style="left:6px;top:4px" width="24" height="24"><rect x="3" y="2" width="14" height="19" fill="#fff" stroke="#bbb" transform="rotate(-12 10 12)"/><rect x="6" y="3" width="14" height="19" fill="#fff" stroke="#aaa"/><path d="M4 6l6 14" stroke="#2a8ae0" stroke-width="3"/></svg>
    <span class="social" style="left:344px;background:#3aa6df"></span>
    <span class="social" style="left:368px;background:#e8761d"></span>
  </div>
  <div class="abs tabs"><span class="on">Lastest</span><span>Articles</span><span>SEO Blog</span><span>Marketing Blog</span><span>Videos</span></div>
  <div class="abs tabs-line"></div>

  <div class="abs news-item" style="top:392px;height:42px">
    <div class="avatar" style="top:4px" role="img" aria-label="Author portrait"></div>
    <div class="kicker" style="top:5px">Blog post</div>
    <div class="title" style="top:15px">Searchly Uses Semantic Closeness as a Ranking Factor</div>
  </div>
  <div class="abs news-item" style="top:434px;height:42px">
    <div class="doc" style="top:10px"></div>
    <div class="kicker" style="top:9px">Articles</div>
    <div class="title" style="top:20px">Do Not Make These 10 Common SEO Mistakes</div>
  </div>
  <div class="abs news-item" style="top:476px;height:62px">
    <div class="avatar" style="top:8px" role="img" aria-label="Author portrait"></div>
    <div class="kicker" style="top:11px">Blog post</div>
    <div class="title" style="top:22px;left:9px;text-indent:24px">Study: Quentrix Reveals Why Consumers Abandon Sites During Checkout</div>
  </div>
  <div class="abs news-item" style="top:538px;height:36px;border-bottom:0">
    <div class="doc" style="top:6px"></div>
    <div class="kicker" style="top:6px">Articles</div>
    <div class="title" style="top:18px">Online Reputation Management Advice</div>
  </div>

  <div class="abs more-box">
    <h4>MORE ARTICLES</h4>
    <ul><li>Search Engine Optimization</li><li>Web design</li><li>Internet marketing</li></ul>
  </div>
</section>

<div class="abs ad" style="left:88px;top:666px;width:298px;height:52px">
  <small>Add</small>
  <div class="ad-fill" style="left:5px;top:12px;width:288px;height:37px">Full Banner<br>468x60</div>
</div>

<!-- resources -->
<section>
  <div class="abs bar res-bar">Resources</div>
  <div class="abs sub-h" style="left:43px;top:773px">Get Listed in the PH Directory Now!</div>
  <div class="abs res-text">If you have a product or service aimed at web professionals, and want to expose yourself to 100,000+ monthly visitors add yourself to the Pagelore-Hub directory.</div>
  <div class="abs tile" style="left:43px">
    <svg class="abs" style="left:27px;top:8px" width="36" height="28"><path d="M2 9h18V2l14 12-14 12v-7H2z" fill="#a8cc2a" stroke="#7a9a10"/></svg>
    Submit your bussiness</div>
  <div class="abs tile" style="left:143px">
    <svg class="abs" style="left:32px;top:6px" width="28" height="30"><path d="M4 26L22 6M6 6l18 20" stroke="#eee" stroke-width="4" stroke-linecap="round"/></svg>
    More webmaster Resources</div>
  <div class="abs latest-h">Lastest resources</div>
  <ul class="abs res-list">
    <li><span class="gear"></span>RSS Parser</li>
    <li><span class="gear"></span>Keyword Density</li>
    <li><span class="gear"></span>Verify Your Site</li>
  </ul>
  <a class="abs more" style="left:43px;top:1028px">See all resources</a>
  <div class="abs rule" style="left:43px;top:1043px;width:189px"></div>
</section>

<!-- forums -->
<section>
  <div class="abs bar forum-bar">Forums</div>
  <div class="abs sub-h" style="left:245px;top:773px">Industry Discussions and Help</div>
  <ul class="abs forum-list">
    <li><svg class="bubble"><path d="M1 1h9v6H4l-3 3z" fill="#2a8ae0"/><path d="M6 5h8v6l-2-2H6z" fill="#a8cc2a"/></svg>Beaten!</li>
    <li><svg class="bubble"><path d="M1 1h9v6H4l-3 3z" fill="#2a8ae0"/><path d="M6 5h8v6l-2-2H6z" fill="#a8cc2a"/></svg>Need SMTP server for mass emailing</li>
    <li><svg class="bubble"><path d="M1 1h9v6H4l-3 3z" fill="#2a8ae0"/><path d="M6 5h8v6l-2-2H6z" fill="#a8cc2a"/></svg>Hosting Options</li>
    <li><svg class="bubble"><path d="M1 1h9v6H4l-3 3z" fill="#2a8ae0"/><path d="M6 5h8v6l-2-2H6z" fill="#a8cc2a"/></svg>Funny Customer Service Inquiries</li>
    <li><svg class="bubble"><path d="M1 1h9v6H4l-3 3z" fill="#2a8ae0"/><path d="M6 5h8v6l-2-2H6z" fill="#a8cc2a"/></svg>What to do you use to develop websites ?</li>
    <li><svg class="bubble"><path d="M1 1h9v6H4l-3 3z" fill="#2a8ae0"/><path d="M6 5h8v6l-2-2H6z" fill="#a8cc2a"/></svg>Pressly Spam</li>
    <li><svg class="bubble"><path d="M1 1h9v6H4l-3 3z" fill="#2a8ae0"/><path d="M6 5h8v6l-2-2H6z" fill="#a8cc2a"/></svg>PH Directory</li>
    <li><svg class="bubble"><path d="M1 1h9v6H4l-3 3z" fill="#2a8ae0"/><path d="M6 5h8v6l-2-2H6z" fill="#a8cc2a"/></svg>36 More SEO Myths</li>
    <li><svg class="bubble"><path d="M1 1h9v6H4l-3 3z" fill="#2a8ae0"/><path d="M6 5h8v6l-2-2H6z" fill="#a8cc2a"/></svg>'Rotating' Newsboard &amp; SEO</li>
    <li><svg class="bubble"><path d="M1 1h9v6H4l-3 3z" fill="#2a8ae0"/><path d="M6 5h8v6l-2-2H6z" fill="#a8cc2a"/></svg>Searchly's new look</li>
  </ul>
  <a class="abs more" style="left:245px;top:1031px">See all discussions</a>
  <div class="abs rule" style="left:245px;top:1043px;width:191px"></div>
</section>

<!-- sidebar -->
<aside>
  <div class="abs ad" style="left:448px;top:135px;width:196px;height:175px">
    <small>Add</small>
    <div class="ad-fill" style="left:5px;top:14px;width:186px;height:156px">Medium Rectangle<br>300x250</div>
  </div>

  <div class="abs text-ads">
    <div class="text-ad"><b>Online Email Marketing</b><p>Expand Your Business Quickly w/ Our User-Friendly Software! Free Trial.</p><em>www.Mailcrest.com</em></div>
    <div class="text-ad"><b>Web site not available ?</b><p>We monitor your web site non-stop. Instant email &amp; sms alert. Reports.</p><em>www.Uptivo.com</em></div>
    <div class="text-ad"><b>Study Digital Marketing</b><p>Norvale Business School Next Round Ends Jun 27th—Apply Now!</p><em>www.Norvale.edu/masters-program/</em></div>
  </div>
  <div class="abs pager"><i></i><i style="background:#1a3fa0"></i><i></i></div>
  <div class="abs" style="left:575px;top:462px;width:49px;height:9px;border:1px solid #ccc"></div>

  <div class="abs bar nl-bar">Get The Latest Online Strategies</div>
  <div class="abs nl-intro">Get all the latest webmaster tips and tricks from some of the brightest minds in the online world delivered right to your inbox with the Pagelore-Hub Newsletter.</div>
  <div class="abs field" style="left:448px;top:564px"><label>Last name:</label><i></i></div>
  <div class="abs field" style="left:448px;top:600px"><label>First name:</label><i></i></div>
  <div class="abs field" style="left:448px;top:636px"><label>Your e-mail:</label><i></i></div>
  <div class="abs privacy">Your <a>privacy</a> is 100% Guaranteed. Easily <a>unsubscribe</a> at any time.</div>
  <div class="abs subscribe">Subscribe me!</div>

  <div class="abs ad" style="left:448px;top:735px;width:196px;height:173px">
    <small>Add</small>
    <div class="ad-fill" style="left:5px;top:14px;width:186px;height:154px">Medium Rectangle<br>300x250</div>
  </div>
  <div class="abs ad" style="left:448px;top:923px;width:196px;height:174px">
    <small>Add</small>
    <div class="ad-fill" style="left:5px;top:14px;width:186px;height:155px">Medium Rectangle<br>300x250</div>
  </div>
</aside>

<footer>
  <div class="abs footer"></div>
  <div class="abs foot-links">Home &nbsp;|&nbsp; Forums &nbsp;|&nbsp; Videos &nbsp;|&nbsp; Articles &nbsp;|&nbsp; Publications &nbsp;|&nbsp; SEO Blog &nbsp;|&nbsp; Marketing Blog &nbsp;|&nbsp; Resources &nbsp;|&nbsp; Advertise &nbsp;|&nbsp; RSS Feeds &nbsp;|&nbsp; Contact Us</div>
  <div class="abs copyright">Copyright 2004 - 2010 Pagelore-Hub.com &nbsp;| <b>Privacy Policy</b> | <b>Affiliate Disclaimer</b></div>
</footer>

</body>
</html>
```